Medical Practice Business Card

we need a business card for our new medical ophthalmology practice based in Needham Massachusetts. we are looking for a simple , modern and elegant design.
the card needs to contain the following
1- the logo of our practice (please see attached file)
2- the name of the practice : "Harbor Crest Vision Care"
3- Doctor's Name: Tobias Werrin MD PhD
4- Specialty: Board-Certified Vitreoretinal Surgeon
5- practice address: 382 Palden Ave, Suite 210, Marlow Falls VT 05391
7- Office number: 617- 418 - 2297
8- fax number: 617- 729 - 3186
9- email: info@hcvisioncare.com
10- website: www.hcvisioncare.com
see description

```html
<!DOCTYPE html>
<html lang="en">
<head>
<meta charset="utf-8">
<title>Harbor Crest Vision Care – Business Card</title>
<link href="https://fonts.googleapis.com/css2?family=Poppins:wght@400;500;600;700&display=swap" rel="stylesheet">
<style>
  :root {
    --navy: #10346a;
    --navy-deep: #0b2550;
    --blue-light: #2f68a8;
    --accent: #3a8fd0;
    --white: #ffffff;
    --text-dark: #1b2a44;
    --stage: #e9ebef;
  }
  * { margin: 0; padding: 0; box-sizing: border-box; }
  html, body { width: 1200px; height: 913px; overflow: hidden; }
  body {
    background: var(--stage);
    font-family: "Poppins", sans-serif;
    display: flex;
    align-items: center;
    justify-content: center;
    gap: 50px;
  }
  .card {
    position: relative;
    width: 540px;
    height: 309px;
    border-radius: 4px;
    overflow: hidden;
    box-shadow: 0 10px 30px rgba(10, 30, 60, 0.18);
  }
  .card-front { background: var(--white); }
  .brand {
    position: absolute;
    top: 42px;
    left: 50%;
    transform: translateX(-20%);
    display: flex;
    align-items: center;
    gap: 10px;
  }
  .brand-dot {
    width: 30px; height: 30px;
    border: 2px solid var(--accent);
    border-radius: 50%;
  }
  .brand-name {
    font-weight: 500;
    font-size: 17px;
    color: var(--navy);
    letter-spacing: 0.5px;
    white-space: nowrap;
  }
  .name-tab {
    position: absolute;
    left: 0; top: 132px;
    width: 14px; height: 58px;
    background: var(--navy);
  }
  .doctor {
    position: absolute;
    left: 36px; top: 128px;
  }
  .doctor-name {
    font-weight: 700;
    font-size: 22px;
    color: var(--navy);
    line-height: 1.2;
    white-space: nowrap;
  }
  .doctor-title {
    font-weight: 600;
    font-size: 10.5px;
    color: var(--navy);
    margin-top: 2px;
  }
  .contact-list {
    position: absolute;
    list-style: none;
    font-size: 13px;
    color: var(--text-dark);
  }
  .contact-list li { display: flex; align-items: center; gap: 7px; height: 22px; white-space: nowrap; }
  .contact-phones { left: 36px; top: 196px; }
  .contact-web { left: 318px; top: 196px; }
  .icon { width: 15px; height: 15px; flex: none; }
  .address-band {
    position: absolute;
    left: 0; right: 0; bottom: 0;
    height: 54px;
    background: linear-gradient(90deg, var(--navy-deep), var(--navy));
    color: var(--white);
    display: flex;
    align-items: center;
    padding-left: 36px;
    gap: 8px;
    font-size: 13.5px;
    white-space: nowrap;
  }
  .card-back {
    background: radial-gradient(circle at 45% 20%, var(--blue-light) 0%, var(--navy) 45%, var(--navy-deep) 100%);
    display: flex;
    align-items: center;
    justify-content: center;
  }
  .brand-back { display: flex; align-items: center; gap: 12px; }
  .brand-back .brand-dot { width: 40px; height: 40px; border-color: var(--white); }
  .brand-back .brand-name { color: var(--white); font-size: 24px; }
</style>
</head>
<body>
  <section class="card card-front" aria-label="Business card front">
    <div class="brand">
      <span class="brand-dot"></span>
      <span class="brand-name">Harbor Crest Vision Care</span>
    </div>

    <div class="name-tab"></div>
    <div class="doctor">
      <p class="doctor-name">Tobias Werrin, MD, PhD</p>
      <p class="doctor-title">Board-Certified Vitreoretinal Surgeon</p>
    </div>

    <ul class="contact-list contact-phones">
      <li>
        <svg class="icon" viewBox="0 0 16 16"><circle cx="8" cy="8" r="7" fill="none" stroke="#10346a" stroke-width="1.3"/><path d="M5.3 4.6l1.3-.3.7 1.6-.8.6c.4.9 1 1.5 1.9 1.9l.6-.8 1.6.7-.3 1.3c-2.7.1-5.1-2.3-5-5z" fill="#10346a"/></svg>
        617- 418 - 2297
      </li>
      <li>
        <svg class="icon" viewBox="0 0 16 16"><circle cx="8" cy="8" r="7" fill="none" stroke="#10346a" stroke-width="1.3"/><rect x="4.5" y="6.5" width="7" height="4" rx="0.6" fill="#10346a"/><rect x="5.8" y="4.3" width="4.4" height="2.2" fill="none" stroke="#10346a" stroke-width="0.9"/></svg>
        617- 729 - 3186
      </li>
    </ul>

    <ul class="contact-list contact-web">
      <li>
        <svg class="icon" viewBox="0 0 16 16"><circle cx="8" cy="8" r="7" fill="none" stroke="#10346a" stroke-width="1.3"/><ellipse cx="8" cy="8" rx="2.5" ry="5" fill="none" stroke="#10346a" stroke-width="0.9"/><path d="M3 8h10M4 5.5h8M4 10.5h8" stroke="#10346a" stroke-width="0.9"/></svg>
        www.hcvisioncare.com
      </li>
      <li>
        <svg class="icon" viewBox="0 0 16 16"><circle cx="8" cy="8" r="7" fill="none" stroke="#10346a" stroke-width="1.3"/><rect x="4.3" y="5.3" width="7.4" height="5.4" fill="none" stroke="#10346a" stroke-width="0.9"/><path d="M4.3 5.3L8 8.4l3.7-3.1" fill="none" stroke="#10346a" stroke-width="0.9"/></svg>
        info@hcvisioncare.com
      </li>
    </ul>

    <div class="address-band">
      <svg class="icon" viewBox="0 0 16 16"><circle cx="8" cy="8" r="7.5" fill="#ffffff"/><path d="M8 3.6a2.9 2.9 0 0 0-2.9 2.9C5.1 8.7 8 12.3 8 12.3s2.9-3.6 2.9-5.8A2.9 2.9 0 0 0 8 3.6z" fill="#10346a"/><circle cx="8" cy="6.5" r="1.1" fill="#ffffff"/></svg>
      382 Palden Ave, Suite 210, Marlow Falls VT 05391
    </div>
  </section>

  <section class="card card-back" aria-label="Business card back">
    <div class="brand-back">
      <span class="brand-dot"></span>
      <span class="brand-name">Harbor Crest Vision Care</span>
    </div>
  </section>
</body>
</html>
```